Trevanix Template Refresh 2017

We want software development managers to remember that presentations using this template showcased Trevanix technology: Our template must be distinctive to be remembered as showing Trevanix technology: They must stand out from the 100s of other tech presentations they see, without being 'wacky', but professional whether bold or subtle. We are targeting the world's largest corporations.

[What do we do?] Trevanix offers the world's first objective, fair measure of software developer productivity (Trevanix Build Gauge) and code quality (Trevanix LUX) metrics.

Our corporate colour is (hex) Red: 13, Green: 10, Blue: 74.

Target Market(s)

CIOs, CTOs and senior software development managers in large Enterprises.

Industry/Entity Type

Information Technology

Font styles to use
Sans Serif

Colors
0355a3

Requirements
Must have
• A memorable design
Nice to have
• Template for slides that will show a view of our User Interface (which shows graphs and charts); ideally a consistent theme to make it clear that this is our own UI, not general graphs and charts to illustrate the presentation. (None of the graphs and charts in the attached presentation are from our User Interface)
• A suggestion would be to make use of our "chord" shape (cut off circle in our logo). This could be white on a blue to appear as a cut-out window for the slide content.
Should not have
• A colourful / jokey / fun tone.

```html
<!DOCTYPE html>
<html lang="de">
<head>
<meta charset="utf-8">
<title>Trevanix – Lorem Ipsum Text</title>
<link href="https://fonts.googleapis.com/css2?family=Arimo:wght@400;700&display=swap" rel="stylesheet">
<style>
  :root {
    --navy: #211f5e;
    --brand-blue: #0355a3;
    --title-blue: #1a56a0;
    --text: #1a1a1a;
    --chart-text: #595959;
    --grid: #d9d9d9;
    --series-1: #1dade3;
    --series-2: #2880c7;
    --series-3: #2accd8;
    --paper: #ffffff;
  }
  * { margin: 0; padding: 0; box-sizing: border-box; }
  html, body { width: 1200px; height: 900px; overflow: hidden; background: var(--paper); }
  .slide {
    position: relative;
    width: 1200px;
    height: 900px;
    overflow: hidden;
    background: var(--paper);
    font-family: "Arimo", Arial, sans-serif;
    color: var(--text);
  }
  .brand {
    position: absolute;
    left: 16px;
    top: 16px;
    display: flex;
    align-items: center;
    gap: 10px;
    color: var(--navy);
    font-weight: 700;
    font-size: 24px;
  }
  .brand-dot {
    width: 34px; height: 34px;
    border-radius: 50%;
    background: var(--navy);
  }
  .side-pillar {
    position: absolute;
    left: 1027px;
    top: 0;
    width: 100px;
    height: 900px;
    background: var(--navy);
    border-radius: 50px 50px 0 0;
  }
  .side-rule { position: absolute; top: 0; height: 900px; background: var(--navy); }
  .side-rule--inner { left: 1149px; width: 11px; }
  .side-rule--outer { left: 1177px; width: 11px; }
  .footer-band {
    position: absolute;
    left: 0;
    top: 802px;
    width: 1127px;
    height: 98px;
    background: linear-gradient(180deg, #27256a 0%, var(--navy) 100%);
  }
  .slide-title {
    position: absolute;
    left: 0;
    width: 1133px;
    top: 118px;
    text-align: center;
    font-weight: 400;
    font-size: 50px;
    color: var(--title-blue);
  }
  .bullets {
    position: absolute;
    left: 40px;
    top: 274px;
    width: 530px;
    list-style: none;
    font-size: 14.6px;
    line-height: 17.6px;
  }
  .bullets li {
    position: relative;
    padding-left: 23px;
    margin-bottom: 17px;
  }
  .bullets li::before {
    content: "";
    position: absolute;
    left: 0;
    top: 6px;
    width: 6px; height: 6px;
    border-radius: 50%;
    background: var(--brand-blue);
  }
  .chart {
    position: absolute;
    left: 600px;
    top: 250px;
    width: 420px;
    height: 440px;
  }
  .chart text { font-family: "Arimo", Arial, sans-serif; fill: var(--chart-text); }
  .chart .grid line { stroke: var(--grid); stroke-width: 1; }
  .s1 { fill: var(--series-1); }
  .s2 { fill: var(--series-2); }
  .s3 { fill: var(--series-3); }
</style>
</head>
<body>
<main class="slide">
  <div class="brand"><span class="brand-dot"></span><span>Trevanix</span></div>

  <div class="side-pillar"></div>
  <div class="side-rule side-rule--inner"></div>
  <div class="side-rule side-rule--outer"></div>
  <div class="footer-band" role="img" aria-label="Dunkelblaues Fußband mit Quadratmuster"></div>

  <h1 class="slide-title">Lorem Ipsum Text</h1>

  <ul class="bullets">
    <li>Mit lieb euren aus meinem freundschaft erste. Das sie erschüttert es das. Ihr ich ihr der entwöhntes zerstreuet steigen die ein.</li>
    <li>Schmerz zauberhauch jugendlich in sie. Herzen getäuscht umwittert herzen ersten lebt liebe. Und sich zauberhauch lied selbst die zug unbekannten. Es es. So zerstoben sang. Herzen entwöhntes lispelnd umwittert strenge ist jenem lied nun herz. Ertönt freundliche sich liebe einer stunden irrt was irren mich meinem.</li>
    <li>Nennt gleich schöne sehnen bang schwankende dunst die und. Menge bilder sie gut gleich. Euch schwebet in und was lieb es sich jenem euch.</li>
    <li>Zerstoben lispelnd lied geisterreich. Entwöhntes wirklichkeiten dem wiederholt denen mein. Ernsten beifall. Herz gesänge ein.</li>
    <li>Mit lieb euren aus meinem freundschaft erste. Das sie erschüttert es das. Ihr ich ihr der entwöhntes zerstreuet steigen die ein. Schmerz zauberhauch jugendlich in sie. Herzen getäuscht umwittert herzen ersten lebt liebe. Und sich zauberhauch lied selbst die zug unbekannten. Es es. So zerstoben sang.</li>
  </ul>

  <svg class="chart" viewBox="600 250 420 440" aria-label="Gestapeltes Säulendiagramm">
    <text x="804" y="294" font-size="27" text-anchor="middle">Chart Title</text>
    <g class="grid">
      <line x1="637" x2="990" y1="579" y2="579"/>
      <line x1="637" x2="990" y1="542.3" y2="542.3"/>
      <line x1="637" x2="990" y1="505.7" y2="505.7"/>
      <line x1="637" x2="990" y1="469" y2="469"/>
      <line x1="637" x2="990" y1="432.4" y2="432.4"/>
      <line x1="637" x2="990" y1="395.7" y2="395.7"/>
      <line x1="637" x2="990" y1="359.1" y2="359.1"/>
      <line x1="637" x2="990" y1="322.5" y2="322.5"/>
    </g>
    <g font-size="19" text-anchor="end">
      <text x="632" y="586">0</text>
      <text x="632" y="549">2</text>
      <text x="632" y="512">4</text>
      <text x="632" y="476">6</text>
      <text x="632" y="439">8</text>
      <text x="632" y="402">10</text>
      <text x="632" y="366">12</text>
      <text x="632" y="329">14</text>
    </g>
    <g>
      <rect class="s1" x="667.5" y="500.1" width="47" height="78.9"/>
      <rect class="s2" x="667.5" y="456.1" width="47" height="44"/>
      <rect class="s3" x="667.5" y="419.4" width="47" height="36.7"/>
      <rect class="s1" x="752.5" y="533.1" width="47" height="45.9"/>
      <rect class="s2" x="752.5" y="452.4" width="47" height="80.7"/>
      <rect class="s3" x="752.5" y="415.7" width="47" height="36.7"/>
      <rect class="s1" x="837.5" y="514.8" width="47" height="64.2"/>
      <rect class="s2" x="837.5" y="481.8" width="47" height="33"/>
      <rect class="s3" x="837.5" y="426.8" width="47" height="55"/>
      <rect class="s1" x="922.5" y="496.5" width="47" height="82.5"/>
      <rect class="s2" x="922.5" y="445.1" width="47" height="51.4"/>
      <rect class="s3" x="922.5" y="353.4" width="47" height="91.7"/>
    </g>
    <g font-size="20" text-anchor="middle">
      <text x="691" y="608">Category</text><text x="691" y="632">1</text>
      <text x="776" y="608">Category</text><text x="776" y="632">2</text>
      <text x="861" y="608">Category</text><text x="861" y="632">3</text>
      <text x="946" y="608">Category</text><text x="946" y="632">4</text>
    </g>
    <g font-size="20">
      <rect class="s1" x="656" y="656" width="10" height="10"/><text x="670" y="669">Series 1</text>
      <rect class="s2" x="764" y="656" width="10" height="10"/><text x="778" y="669">Series 2</text>
      <rect class="s3" x="871" y="656" width="10" height="10"/><text x="885" y="669">Series 3</text>
    </g>
  </svg>
</main>
</body>
</html>
```